Flyer Designer for a Widow and Door Company - loooking for fresh design

We are looking for a flyer designed to advertise our business - we supply and install windows and doors - we are looking for a fresh looking flyer to distribute to drum up business - more information can be found at our website www.brightpanehouse.co.uk - We want a different approach than we currently have - making it vibrant and fresh - you can see the services on the website but its more the graphical design that we are looking for rather than content as the content from the website can be used for each service etc.

Target Market(s)

the general public

Colors

Designer to choose colors to be used in the design.

Requirements
Must have
• vibrant design and images

```html
<!DOCTYPE html>
<html lang="en">
<head>
<meta charset="utf-8">
<title>Bright Pane House – Flyer</title>
<link rel="stylesheet" href="https://fonts.googleapis.com/css2?family=Source+Sans+3:wght@400;600;700&display=swap">
<style>
  :root{
    --blue:#2e74b0;
    --green:#6fbe1f;
    --grey:#d4d4d4;
    --ink:#1a1a1a;
    --white:#ffffff;
    --frame:#1c1c1c;
    --icon-ring:#8a8f96;
  }
  *{margin:0;padding:0;box-sizing:border-box}
  html,body{width:1200px;height:1200px;overflow:hidden;background:var(--white)}
  body{font-family:"Source Sans 3",sans-serif;color:var(--ink)}
  .stage{position:absolute;left:0;top:0;width:1920px;height:1920px;transform:scale(.625);transform-origin:0 0}
  .flyer{position:absolute;left:455px;top:243px;width:1023px;height:1447px;border:2px solid var(--frame);overflow:hidden;background:var(--white)}
  .shapes{position:absolute;left:0;top:0;width:1023px;height:1447px}
  .abs{position:absolute}

  .brand{left:30px;top:42px;display:flex;align-items:center;gap:18px}
  .brand-mark{width:110px;height:110px;background:var(--blue)}
  .brand-name{font-size:44px;font-weight:700;color:var(--blue);line-height:1}
  .brand-tag{font-size:17px;font-weight:700;color:var(--blue);letter-spacing:.5px;margin-top:10px}

  .headline{left:0;top:453px;width:621px;height:111px;background:var(--blue);color:var(--white);
    font-weight:700;font-size:31px;line-height:41px;text-align:center;padding-top:15px;padding-left:40px}

  .who{right:44px;top:618px;text-align:right;color:var(--white);font-size:19px;line-height:22.7px}
  .who h2{font-size:21px;font-weight:700;line-height:28px}

  .service{left:110px;width:452px;font-size:19px;line-height:22.7px;text-align:justify}
  .service h3{font-size:21px;font-weight:700;color:var(--blue);line-height:25px}
  .service-icon{left:33px;width:64px;height:64px;border-radius:50%;background:var(--blue);border:3px solid var(--icon-ring)}
  .service-icon svg{width:100%;height:100%}

  .why{right:48px;top:906px;text-align:right;font-size:19px;line-height:22.7px}
  .why h3{font-size:21px;font-weight:700;color:var(--blue);line-height:25px}
  .benefits{list-style:none;margin-top:6px}
  .benefits li{line-height:24px;display:flex;justify-content:flex-end;align-items:center;gap:8px}
  .tick{width:19px;height:19px;flex:none}

  .call{left:140px;top:1338px;display:flex;align-items:center;gap:20px;color:var(--white)}
  .phone-number{font-size:46px;font-weight:700;line-height:46px}
  .web{font-size:20px;font-weight:700;margin-top:4px;padding-left:6px}
  .address{left:760px;top:1305px;width:200px;text-align:center;color:var(--white);font-size:15.5px;line-height:18.7px}
  .address strong{font-size:17px}
</style>
</head>
<body>
<div class="stage">
  <div class="flyer">
    <svg class="shapes" viewBox="0 0 1023 1447">
      <defs>
        <linearGradient id="photoTone" x1="0" y1="0" x2="1" y2="1">
          <stop offset="0" stop-color="#a8aaa4"/>
          <stop offset=".45" stop-color="#6f7570"/>
          <stop offset="1" stop-color="#b9b6ab"/>
        </linearGradient>
      </defs>
      <polygon role="img" aria-label="Photo of grey stone house wall with dark framed windows, blinds and flower boxes" points="0,239 1023,112 1023,544 0,712" fill="url(#photoTone)"/>
      <polygon points="0,712 152,687 242,710 0,1007" fill="var(--grey)"/>
      <polygon points="150,687 1023,544 1023,887" fill="var(--green)"/>
      <polygon points="0,1342 1023,1262 1023,1447 0,1447" fill="var(--blue)"/>
    </svg>

    <div class="abs brand">
      <div class="brand-mark"></div>
      <div>
        <div class="brand-name">BRIGHT PANE HOUSE</div>
        <div class="brand-tag">BESPOKE WINDOWS &amp; DOORS</div>
      </div>
    </div>

    <div class="abs headline">TRANSFORM THE LOOK OF YOUR HOME<br>WITH THE NEW WINDOWS AND DOORS</div>

    <div class="abs who">
      <h2>Who we are</h2>
      <p>Bright Pane House are Suppliers and installers of<br>quality windows and doors across Northamptonshire<br>and surrounding villages. Offering a friendly, customer<br>focused approach to your replacement windows and doors.<br>Providing a full colour range of uPVc and aluminium to<br>compliment any home.</p>
    </div>

    <div class="abs service-icon" style="top:789px">
      <svg viewBox="0 0 64 64"><rect x="21" y="17" width="22" height="30" fill="none" stroke="#fff" stroke-width="3"/><line x1="32" y1="17" x2="32" y2="47" stroke="#fff" stroke-width="3"/><line x1="21" y1="30" x2="43" y2="30" stroke="#fff" stroke-width="3"/></svg>
    </div>
    <div class="abs service" style="top:766px">
      <h3>Our Windows</h3>
      <p>Our windows are individually designed to suit your home. With an extensive choice of styles, colours and finishes, our windows offer an exceptional level of energy efficency with market leading locking systems.</p>
    </div>

    <div class="abs service-icon" style="top:928px">
      <svg viewBox="0 0 64 64"><rect x="23" y="15" width="19" height="33" fill="none" stroke="#fff" stroke-width="3"/><polygon points="23,15 33,19 33,51 23,48" fill="#fff"/><circle cx="30" cy="33" r="1.5" fill="var(--blue)"/></svg>
    </div>
    <div class="abs service" style="top:902px">
      <h3>Our Doors</h3>
      <p>With literally hundreds of different designs, colours and finishes to choose from, our doors can transform the look of your home, offer increased thermal efficiency and dramatically improve security for your peace of mind.</p>
    </div>

    <div class="abs service-icon" style="top:1054px">
      <svg viewBox="0 0 64 64"><line x1="18" y1="18" x2="46" y2="46" stroke="#fff" stroke-width="4" stroke-linecap="round"/><line x1="46" y1="18" x2="18" y2="46" stroke="#fff" stroke-width="4" stroke-linecap="round"/><circle cx="46" cy="18" r="5" fill="none" stroke="#fff" stroke-width="3"/></svg>
    </div>
    <div class="abs service" style="top:1038px">
      <h3>Repairs</h3>
      <p>We offer a full repair and replacement service on glass units, windows and doors. Please contact one of our helpful advisors for a non obligatory quotation.</p>
    </div>

    <div class="abs service-icon" style="top:1186px">
      <svg viewBox="0 0 64 64"><polygon points="32,15 50,31 45,31 45,48 36,48 36,39 28,39 28,48 19,48 19,31 14,31" fill="#fff"/></svg>
    </div>
    <div class="abs service" style="top:1150px">
      <h3>Landlord Services</h3>
      <p>We work closely with Landlords &amp; Letting Agents to offer a full repair or replacement service on glass units, windows and doors. We also offer property surveys and recommendations on the condition of the current windows and doors.</p>
    </div>

    <div class="abs why">
      <h3>Why choose us</h3>
      <p>At Bright Pane House we offer the following<br>benefits as standard on all of our products<br>for your peace of mind.</p>
      <ul class="benefits">
        <li><svg class="tick" viewBox="0 0 20 20"><circle cx="10" cy="10" r="10" fill="var(--blue)"/><polyline points="5,10 9,14 15,6" fill="none" stroke="#fff" stroke-width="2.4"/></svg>Registered installer</li>
        <li><svg class="tick" viewBox="0 0 20 20"><circle cx="10" cy="10" r="10" fill="var(--blue)"/><polyline points="5,10 9,14 15,6" fill="none" stroke="#fff" stroke-width="2.4"/></svg>Additional security</li>
        <li><svg class="tick" viewBox="0 0 20 20"><circle cx="10" cy="10" r="10" fill="var(--blue)"/><polyline points="5,10 9,14 15,6" fill="none" stroke="#fff" stroke-width="2.4"/></svg>A rated energy efficient</li>
        <li><svg class="tick" viewBox="0 0 20 20"><circle cx="10" cy="10" r="10" fill="var(--blue)"/><polyline points="5,10 9,14 15,6" fill="none" stroke="#fff" stroke-width="2.4"/></svg>Proudly made in The United Kingdom</li>
        <li><svg class="tick" viewBox="0 0 20 20"><circle cx="10" cy="10" r="10" fill="var(--blue)"/><polyline points="5,10 9,14 15,6" fill="none" stroke="#fff" stroke-width="2.4"/></svg>Precision made to measure</li>
        <li><svg class="tick" viewBox="0 0 20 20"><circle cx="10" cy="10" r="10" fill="var(--blue)"/><polyline points="5,10 9,14 15,6" fill="none" stroke="#fff" stroke-width="2.4"/></svg>Competitive pricing</li>
        <li><svg class="tick" viewBox="0 0 20 20"><circle cx="10" cy="10" r="10" fill="var(--blue)"/><polyline points="5,10 9,14 15,6" fill="none" stroke="#fff" stroke-width="2.4"/></svg>10 years guarantee</li>
        <li><svg class="tick" viewBox="0 0 20 20"><circle cx="10" cy="10" r="10" fill="var(--blue)"/><polyline points="5,10 9,14 15,6" fill="none" stroke="#fff" stroke-width="2.4"/></svg>Friendly professional staff</li>
        <li><svg class="tick" viewBox="0 0 20 20"><circle cx="10" cy="10" r="10" fill="var(--blue)"/><polyline points="5,10 9,14 15,6" fill="none" stroke="#fff" stroke-width="2.4"/></svg>No obligation quotes</li>
      </ul>
    </div>

    <div class="abs call">
      <svg width="118" height="82" viewBox="0 0 118 82">
        <path d="M4,34 C4,8 114,8 114,34 L114,40 L88,40 L88,30 C76,24 42,24 30,30 L30,40 L4,40 Z" fill="#fff"/>
        <path d="M22,44 C26,30 92,30 96,44 L100,72 C100,80 18,80 18,72 Z" fill="#fff"/>
        <ellipse cx="59" cy="55" rx="19" ry="15" fill="var(--blue)"/>
      </svg>
      <div>
        <div class="phone-number">01632 960 418</div>
        <div class="web">www.brightpanehouse.co.uk</div>
      </div>
    </div>

    <div class="abs address">
      <strong>Bright Pane House Ltd</strong><br>
      Millbrook House<br>
      Canal Lane<br>
      Ashcombe<br>
      Northamptonshire<br>
      NN0 4ZX
    </div>
  </div>
</div>
</body>
</html>
```